Firm of surveyors needs a professional yet friendly looking flyer

Our company offers help to landlords who have a phone mast on their property. We help them to negotiate the best rent and lease terms. There are so many landlords who don't seek professional advice because they don't know it's available. We want to send them a flyer which is informative, looks professional but also friendly so it prompts them to call us. I have attached the wording and some pictures but have more I can send but they were too large to attach.

Target Market(s)

Ranges from farmers to large corporations and land owners

Industry/Entity Type

Surveyor

Font styles to use
Sans Serif

Colors
acd136
9bcb3c
000000
ffffff
606060
848484

Requirements
Must have
• Must be clear, must give a professional look, must include pictures, must include our logo, must use our colour scheme (or variations of it). Ideally, I would like a try-fold design if possible.
Nice to have
• I would like there to be stand out lines to catch the readers eye (I have included some on the wording document). I would like a clean and modern design
Should not have
• Should not be too fussy

```html
<!DOCTYPE html>
<html lang="en">
<head>
<meta charset="utf-8">
<title>Mastwise Surveyors – Tri-fold Flyer</title>
<link href="https://fonts.googleapis.com/css2?family=Montserrat:wght@300;400;500;600&display=swap" rel="stylesheet">
<style>
  :root{
    --green:#9bcb3c;
    --green-light:#acd136;
    --ink:#2b2b2d;
    --black:#000000;
    --white:#ffffff;
    --grey:#606060;
    --grey-light:#848484;
    --sky-top:#ffffff;
    --sky-mid:#3f6fc0;
    --sky-deep:#0d3a9a;
  }
  *{margin:0;padding:0;box-sizing:border-box}
  html,body{width:1200px;height:848px;overflow:hidden;background:var(--white)}
  .flyer{position:relative;width:1200px;height:848px;overflow:hidden;font-family:"Montserrat",Arial,sans-serif;color:var(--ink)}
  .flyer__shapes{position:absolute;inset:0;width:1200px;height:848px}
  .copy{position:absolute;font-size:12.6px;line-height:17px;font-weight:300;text-align:justify}
  .copy p{margin-bottom:6px}
  .copy--left{left:25px;top:86px;width:348px;color:var(--ink)}
  .copy--centre{left:426px;top:86px;width:366px;color:var(--white)}
  .copy--right{left:817px;top:122px;width:363px;color:var(--ink)}
  .section-title{font-weight:600;font-size:23px;line-height:27px;color:var(--white);display:inline-block;
    white-space:nowrap;text-align:left;border-bottom:2px solid var(--white);padding:0 6px 2px 0;margin-bottom:7px;letter-spacing:0}
  .section-title + p{margin-bottom:9px}
  .callout{font-weight:500;font-size:14px;line-height:19px;text-align:center;color:var(--black);
    border-top:1.5px solid var(--ink);border-bottom:1.5px solid var(--ink);padding:3px 0 4px;margin:4px 0 9px}
  .prompt{text-align:justify;margin-bottom:9px;font-size:12.8px}
</style>
</head>
<body>
<main class="flyer">
  <svg class="flyer__shapes" viewBox="0 0 1300 919" preserveAspectRatio="none">
    <defs>
      <linearGradient id="sky" x1="0" y1="0" x2="0" y2="1">
        <stop offset="0" stop-color="var(--sky-top)"/>
        <stop offset="0.18" stop-color="var(--sky-mid)"/>
        <stop offset="1" stop-color="var(--sky-deep)"/>
      </linearGradient>
    </defs>
    <rect class="photo photo--lattice-mast" x="0" y="262" width="440" height="620" fill="url(#sky)" role="img" aria-label="Photo of a lattice phone mast with antennas against a blue sky"/>
    <rect class="photo photo--pole-mast" x="875" y="500" width="425" height="380" fill="url(#sky)" role="img" aria-label="Photo of a slim white phone mast with antennas against a blue sky"/>
    <polygon class="band band--dark" points="0,0 560,0 440,35 0,80" fill="var(--ink)"/>
    <polygon class="band band--green" points="480,0 1300,0 1300,14 860,106" fill="var(--green)"/>
    <polygon class="band band--dark" points="880,108 1300,22 1300,88 1140,110" fill="var(--ink)"/>
    <polygon class="panel panel--centre" points="438,36 560,28 875,100 875,838 860,846 438,910" fill="var(--ink)"/>
    <polygon class="band band--dark" points="0,858 438,900 438,919 0,919" fill="var(--ink)"/>
    <polygon class="band band--green" points="600,919 875,846 1300,910 1300,919" fill="var(--green)"/>
  </svg>

  <section class="copy copy--left">
    <p>Recently, operators have been attempting to cut costs by reducing rents. They are joining forces in an effort to drive rents down. Many landlords are contacting us after receiving a letter from the operators / operator’s agent, telling them they must accept a rent reduction or risk losing their site. In the majority of cases, Mastwise Surveyors can prevent this from occurring and protect the landlord’s rental income.</p>
  </section>

  <section class="copy copy--centre">
    <h2 class="section-title">Sell Your Phone Mast</h2>
    <p>We can also assist landlords in selling their phone mast. We have strong links with many large investors who regularly purchase the freehold or leasehold interest of masts and will pay a cash lump sum of tens, even hundreds of thousands of pounds. This can be done in a matter of weeks and the cash is yours to spend however you like, regardless of whether the mast stays for the duration of the investors leasehold or not. We can negotiate flexible terms, such as a buyback option so please call us today to discuss.</p>
    <h2 class="section-title">Getting A Phone Mast</h2>
    <p>If you don’t currently have a mast located on your land but are interested in receiving thousands of pounds a year in rental income, or you have a redundant mast you would like to market, we offer a free advertising service on our website. We will market your land to phone mast operators with a view to having a mast located there. Please visit the ‘Advertise My Site’ link on our website to take advantage of this service.</p>
    <h2 class="section-title">The Current Telecoms Climate</h2>
    <p>The telecoms market, in relation to mobile phone masts, is going through some huge changes. Operators are combining to cut costs. We have already seen Trio Mobile join forces with Telara and Oxyn form a jointly owned company with Voxalink called CMIL. More recently, Telara and Citrus Mobile have merged to form Allway Networks Ltd to become the new network leader. What this can mean for the landlord is changes to their site and potentially the loss of income. It can all be very confusing but don’t worry, this is where we can help. We know the telecoms industry and understand how a new situation may affect a landlord, therefore, allowing us to provide the best advice on protecting your asset.</p>
  </section>

  <section class="copy copy--right">
    <p>In April 2017, the Government introduced the Digital Economy Act. This sets out significant changes for landlords, including the way rents are calculated. We have already seen operators contact landlords, trying to reduce their rent in light of this new law. We are working alongside specialist telecoms solicitors to try to reduce the potential negative impact on landlords.</p>
    <p class="callout">Landlords Should Not Sign Anything Until They Have Sought Professional Advice</p>
    <p class="prompt">Unsure Whether You Are Getting The Best Rent? Call Us Now For A Free, No Obligation Chat</p>
    <p class="prompt">Our Expert Surveyors Will Be Happy To Help You Understand Proposed Changes And What They Could Mean For You</p>
    <p class="prompt">Interested In Selling Your Site? Or Already Have An Offer? We Can Help You To Achieve The Best Sale Price, Quickly</p>
  </section>
</main>
</body>
</html>
```